Label - Australian Extra Virgin Olive Oil

I'm seeking a front and back label to apply to bottles/tins of my olive oil. They will be applied to green bottles of various sizes and also white tins. The labels will have the dimensions 70 x 120mm and printed at 600dpi on adhesive labels with metalised backing. With this material, any area which is not colored on the label will show through as silver - the design may make use of this feature. There are some obligatory labeling requirements in Australia including a logo showing the proportion of Australian content, and an indication of the harvest date - the design will need to make allowance for this. Also, since the label will be used in subsequent years and on various sizes of product, I need to be able to alter this with each print run.I have a logo to use on the front label and another I would like to use on the back as this latter one will tie in with other future products (non olive oil).
The text for the back label
"Tallowind Creek is a family run enterprise. Our olives are grown on the banks of the Yarrabell River in Central Victoria and processed locally
email; swiftwombat@kelpo.com.au
text needed for the front label design
"Australian Extra-Virgin Olive Oil"

```html
<!DOCTYPE html>
<html lang="en">
<head>
<meta charset="utf-8">
<title>Tallowind Creek – Australian Extra Virgin Olive Oil Label</title>
<link rel="stylesheet" href="https://fonts.googleapis.com/css2?family=Montserrat:wght@500;700;800&display=swap">
<style>
  :root {
    --page-bg: #ffffff;
    --label-dark: #27351a;
    --label-mid: #46582a;
    --label-light: #6b7a3a;
    --leaf-green: #8dc63f;
    --ink-white: #ffffff;
    --ink-dark: #1c2612;
    --shield-black: #111111;
    --brand-cream: #f3dcae;
  }
  html, body {
    margin: 0;
    padding: 0;
    width: 1200px;
    height: 1000px;
    overflow: hidden;
    background: var(--page-bg);
  }
  .canvas {
    display: block;
    width: 1200px;
    height: 1000px;
  }
  .label-text {
    font-family: "Montserrat", sans-serif;
  }
  .brand-name {
    fill: var(--brand-cream);
    font-weight: 700;
    font-size: 30px;
  }
  .origin-word {
    fill: var(--ink-white);
    stroke: var(--ink-dark);
    stroke-width: 6px;
    paint-order: stroke;
    font-weight: 800;
    font-size: 66px;
  }
  .grade-word {
    fill: var(--ink-white);
    font-weight: 700;
    font-size: 92px;
  }
  .product-word {
    fill: var(--ink-white);
    font-weight: 700;
    font-size: 78px;
  }
  .harvest-caption {
    fill: var(--ink-dark);
    font-weight: 500;
    font-size: 17px;
  }
</style>
</head>
<body>
<svg class="canvas" viewBox="0 0 1200 1000" xmlns="http://www.w3.org/2000/svg">
  <defs>
    <radialGradient id="olive-photo-tone" cx="50%" cy="55%" r="70%">
      <stop offset="0" stop-color="#6b7a3a"/>
      <stop offset="0.45" stop-color="#46582a"/>
      <stop offset="1" stop-color="#27351a"/>
    </radialGradient>
    <clipPath id="label-shape">
      <path d="M370,12 H831 A42,42 0 0 0 873,54 V943 A42,42 0 0 0 831,985 H370 A42,42 0 0 0 328,943 V54 A42,42 0 0 0 370,12 Z"/>
    </clipPath>
    <path id="star" d="M0,-13 L3.8,-4.2 L12.4,-4 L5.6,2.2 L7.7,11 L0,6.2 L-7.7,11 L-5.6,2.2 L-12.4,-4 L-3.8,-4.2 Z"/>
  </defs>

  <!-- Label body -->
  <g class="label" clip-path="url(#label-shape)">
    <rect class="label-photo" x="328" y="12" width="545" height="973" fill="url(#olive-photo-tone)"
          role="img" aria-label="Photo of green olives glistening with golden olive oil pouring down"/>

    <!-- Inner frame -->
    <path class="label-frame" fill="none" stroke="var(--leaf-green)" stroke-width="4"
          d="M414,45 H787 A62,62 0 0 0 849,107 V893 A62,62 0 0 0 787,955 H414 A62,62 0 0 0 352,893 V107 A62,62 0 0 0 414,45 Z"/>

    <!-- Brand name -->
    <circle class="brand-dot" cx="600" cy="100" r="14" fill="var(--brand-cream)"/>
    <text class="label-text brand-name" x="600" y="160" text-anchor="middle">Tallowind Creek</text>

    <!-- Origin band -->
    <rect class="origin-band" x="328" y="222" width="545" height="93" fill="var(--leaf-green)"/>
    <text class="label-text origin-word" x="390" y="294" textLength="420" lengthAdjust="spacingAndGlyphs">AUSTRALIAN</text>

    <!-- Grade -->
    <text class="label-text grade-word" x="428" y="407" textLength="344" lengthAdjust="spacingAndGlyphs">EXTRA</text>
    <line class="grade-rule" x1="408" y1="416" x2="795" y2="416" stroke="var(--leaf-green)" stroke-width="4"/>
    <text class="label-text grade-word" x="430" y="498" textLength="350" lengthAdjust="spacingAndGlyphs">VIRGIN</text>

    <!-- Rating stars -->
    <g class="rating-stars" fill="var(--leaf-green)">
      <use href="#star" x="513" y="535"/>
      <use href="#star" x="556" y="535"/>
      <use href="#star" x="599" y="535"/>
      <use href="#star" x="642" y="535"/>
      <use href="#star" x="685" y="535"/>
    </g>

    <!-- Product shield -->
    <path class="product-shield" fill="var(--shield-black)" stroke="var(--leaf-green)" stroke-width="4"
          d="M454,580 Q600,552 746,580 L746,690 Q746,792 600,828 Q454,792 454,690 Z"/>
    <text class="label-text product-word" x="478" y="682" textLength="240" lengthAdjust="spacingAndGlyphs">OLIVE</text>
    <text class="label-text product-word" x="531" y="752" textLength="135" lengthAdjust="spacingAndGlyphs">OIL</text>

    <!-- Origin content badge placeholder -->
    <rect class="origin-badge" x="368" y="800" width="62" height="85" rx="3" fill="var(--ink-white)" stroke="var(--leaf-green)" stroke-width="2"/>
    <rect class="origin-badge-mark" x="380" y="810" width="38" height="44" fill="#2e8b3a"/>

    <!-- Harvest date field -->
    <rect class="harvest-field" x="452" y="857" width="294" height="40" rx="20" fill="var(--ink-white)"/>
    <text class="label-text harvest-caption" x="470" y="883">Harvest date :</text>
  </g>
</svg>
</body>
</html>
```